Monument sign* - Law Firm

*I am installing a monument sign that has LED, as well as backlit elements. I am seeking help in designing the backlit portion of the sign. The Backlit sign will be 12’ x 4’.

We are looking for a classic, yet eye-catching sign to help new and current clients find our firm as well as bring in future clients. One of our goals is that people who drive by on a regular basis remember our sign (and us) for any future legal need.

Target Market(s)

Current and future clientele

Industry/Entity Type

Law Firm

Font styles to use
Serif
Sans Serif

Colors
b1b1b1
333333

Requirements
Must have
• Business name: Hargrove Law Firm, Inc.
• Website: www.hargrovelawfirm-example.com
• Telephone: (555)214-3679
• Our firm's logo
Nice to have
• Color preference is black, taupe, and white. A photo for reference of the office coloring is uploaded.
• We currently have an established logo which our firm has been using for more than 10 years. Our logo has been used in advertising, commercials, letterhead, and on-site. We are looking to transition from brown/rust/cream to the black/taupe/white color scheme.
Should not have
• Cheesy slogans; character designs; directions; additional symbols outside of the firm's logo.

```html
<!DOCTYPE html>
<html lang="en">
<head>
<meta charset="utf-8">
<title>Hargrove Law Firm, Inc. – Monument Sign</title>
<link rel="stylesheet" href="https://fonts.googleapis.com/css2?family=Oswald:wght@500&family=Montserrat:wght@700&display=swap">
<style>
  :root {
    --backdrop: #c9c9c9;
    --ink: #1f1f1f;
    --charcoal: #333333;
    --taupe: #c2b196;
    --silver: #b1b1b1;
    --panel-top: #ffffff;
    --panel-bottom: #e4e4e4;
    --photo-sky: #d9dde0;
    --photo-stucco: #8a8275;
    --photo-green: #55703d;
  }
  * { margin: 0; padding: 0; box-sizing: border-box; }
  html, body { width: 1200px; height: 1000px; overflow: hidden; }
  body { background: var(--backdrop); position: relative; }

  .sign {
    position: absolute;
    left: 40px; top: 313px;
    width: 1120px; height: 373px;
    box-shadow: 0 22px 26px -14px rgba(0,0,0,0.45);
  }
  .sign-shapes { position: absolute; inset: 0; }

  .logo-block {
    position: absolute;
    left: 296px; top: 40px;
    width: 72px;
    display: flex; flex-direction: column; align-items: center; gap: 6px;
  }
  .logo-square { width: 58px; height: 58px; background: var(--taupe); }
  .logo-name {
    font-family: "Oswald", sans-serif; font-weight: 500;
    font-size: 14px; letter-spacing: 1px; color: var(--charcoal);
    text-transform: uppercase;
  }

  .firm-name {
    position: absolute;
    left: 384px; top: 42px;
    font-family: "Oswald", sans-serif; font-weight: 500;
    font-size: 64px; line-height: 1;
    color: var(--ink); text-transform: uppercase;
    white-space: nowrap; letter-spacing: 0.5px;
  }

  .contact-line {
    position: absolute;
    left: 300px; right: 0;
    display: flex; align-items: center; justify-content: center; gap: 12px;
    font-family: "Montserrat", sans-serif; font-weight: 700;
    color: var(--ink); white-space: nowrap;
  }
  .contact-phone { top: 185px; height: 73px; font-size: 44px; letter-spacing: 1px; }
  .contact-web { top: 258px; height: 115px; font-size: 35px; }
  .contact-icon { flex: none; }
</style>
</head>
<body>
  <div class="sign">
    <svg class="sign-shapes" width="1120" height="373" viewBox="0 0 1120 373">
      <defs>
        <linearGradient id="panelGrad" x1="0" y1="0" x2="0" y2="1">
          <stop offset="0" stop-color="var(--panel-top)"/>
          <stop offset="1" stop-color="#efefef"/>
        </linearGradient>
        <linearGradient id="lowerGrad" x1="0" y1="0" x2="0" y2="1">
          <stop offset="0" stop-color="#ececec"/>
          <stop offset="1" stop-color="var(--panel-bottom)"/>
        </linearGradient>
        <linearGradient id="photoGrad" x1="0" y1="0" x2="0" y2="1">
          <stop offset="0" stop-color="var(--photo-sky)"/>
          <stop offset="0.25" stop-color="var(--photo-stucco)"/>
          <stop offset="0.85" stop-color="#6e675d"/>
          <stop offset="1" stop-color="var(--photo-green)"/>
        </linearGradient>
      </defs>
      <rect class="panel-upper" x="0" y="0" width="1120" height="185" fill="url(#panelGrad)"/>
      <rect class="band-phone" x="0" y="185" width="1120" height="73" fill="var(--taupe)"/>
      <rect class="panel-lower" x="0" y="258" width="1120" height="115" fill="url(#lowerGrad)"/>
      <polygon class="divider-stripe" points="238,0 264,0 300,373 274,373" fill="var(--silver)"/>
      <polygon class="office-photo" role="img" aria-label="Photo of the firm's stucco office building with dark roof, arched entry and landscaped garden"
               points="0,0 240,0 276,373 0,373" fill="url(#photoGrad)"/>
    </svg>

    <div class="logo-block">
      <div class="logo-square"></div>
      <div class="logo-name">Hargrove</div>
    </div>

    <div class="firm-name">Hargrove Law Firm, Inc.</div>

    <div class="contact-line contact-phone">
      <svg class="contact-icon" width="40" height="40" viewBox="0 0 40 40" aria-hidden="true">
        <circle cx="20" cy="20" r="20" fill="var(--ink)"/>
        <path d="M14 10c1-1 2.5-1 3.2.2l2 3.3c.5.9.3 2-.5 2.6l-1.5 1.1c1 2.3 2.8 4.2 5.1 5.3l1.2-1.5c.6-.8 1.7-1 2.6-.5l3.3 2c1.2.7 1.2 2.2.2 3.2l-1.6 1.6c-1.3 1.3-3.3 1.6-5 .8C17.7 26.1 13.9 22.3 12 17.1c-.7-1.7-.4-3.7.9-5z" fill="#fff"/>
      </svg>
      <span>(555) 214-3679</span>
    </div>

    <div class="contact-line contact-web">
      <svg class="contact-icon" width="34" height="34" viewBox="0 0 34 34" aria-hidden="true" fill="none" stroke="var(--ink)" stroke-width="2.2">
        <circle cx="17" cy="17" r="15"/>
        <ellipse cx="17" cy="17" rx="6.5" ry="15"/>
        <line x1="2" y1="17" x2="32" y2="17"/>
        <path d="M5 9.5h24M5 24.5h24"/>
      </svg>
      <span>www.hargrovelawfirm-example.com</span>
    </div>
  </div>
</body>
</html>
```